Brixel Solutions Website Creation

Create a business website for custom flexible packaging and MDF products. The www.Olvane.com website is generic page that you can use to create a similar home page for my business.
Specifically: https://www.olvane.com/packaging/
https://www.olvane.com/product/mdf-panels/
Domain is Brix-El.com
I would like the page to have a more packaging related look than the MDF/wood.

```html
<!DOCTYPE html>
<html lang="en">
<head>
<meta charset="utf-8">
<title>Brixel Solutions — Custom Flexible Packaging &amp; MDF Products</title>
<link href="https://fonts.googleapis.com/css2?family=DM+Sans:wght@400;500;600;700&family=Roboto:wght@400;500;700&display=swap" rel="stylesheet">
<style>
:root{
  --navy:#1f2a4a;
  --navy-deep:#1a2340;
  --blue:#10a0f2;
  --blue-soft:#3aa7ea;
  --slate:#4a5577;
  --ink:#24304f;
  --text:#3b3f4a;
  --white:#ffffff;
}
*{box-sizing:border-box;margin:0;padding:0}
html,body{width:1200px;height:3825px;overflow:hidden}
body{position:relative;background:var(--white);font-family:"DM Sans",sans-serif;color:var(--text)}
.abs{position:absolute}
a{text-decoration:none;color:inherit}

/* header */
.site-header{left:0;top:0;width:1200px;height:116px;background:var(--white)}
.brand{display:flex;align-items:center;gap:12px;white-space:nowrap}
.brand-dot{width:50px;height:50px;border-radius:50%;background:var(--blue);flex:none}
.brand-name{font-family:"DM Sans",sans-serif;font-weight:600;font-size:28px;color:var(--ink);letter-spacing:.3px}
.site-header .brand{left:111px;top:33px}
.main-nav{left:429px;top:48px;display:flex;gap:21px;font-family:"Roboto",sans-serif;font-size:17px;color:var(--ink);text-transform:uppercase;white-space:nowrap}
.main-nav .active{color:var(--blue)}
.search-icon{left:1066px;top:50px}

/* hero */
.hero{left:0;top:116px;width:1200px;height:694px}
.hero-copy{left:111px;width:620px;color:var(--white)}
.hero-title{font-family:"DM Sans",sans-serif;font-size:54px;line-height:69px;font-weight:700}
.hero-title .light{font-weight:400}
.hero-title .accent{color:var(--blue)}
.hero-lead{font-size:16px;line-height:26px;margin-top:22px;width:570px}
.btn{display:inline-flex;align-items:center;justify-content:center;width:229px;height:51px;border-radius:5px;font-family:"Roboto",sans-serif;font-weight:500;font-size:17px;color:var(--white);background:var(--blue);text-transform:uppercase}
.btn.dark{background:var(--navy)}
.hero .btn{margin-top:34px}

/* intro */
.eyebrow{font-family:"Roboto",sans-serif;font-size:16px;color:var(--blue);text-transform:uppercase;letter-spacing:.3px}
.intro{left:0;top:902px;width:1200px;text-align:center}
.intro h2{font-family:"Roboto",sans-serif;font-size:45px;line-height:53px;font-weight:700;color:var(--ink);margin-top:18px}
.intro p{width:810px;margin:30px auto 0;font-size:16px;line-height:26px}
.category{top:1188px;width:229px}
.category .thumb{height:235px;border-radius:6px 6px 0 0}
.category .label{margin-top:4px;height:52px;border-radius:0 0 6px 6px;background:var(--navy);color:var(--white);display:flex;align-items:center;justify-content:center;font-weight:600;font-size:17px}
.category .label.hl{background:var(--blue)}

/* band */
.band{left:0;top:1593px;width:1200px;height:474px;background:var(--navy)}
.band-photo{left:700px;top:0;width:500px;height:474px;background:linear-gradient(90deg,var(--navy) 0%,#4b5a5a 55%,#8a9a3a 100%)}
.section-title{font-family:"Roboto",sans-serif;font-weight:700;font-size:30px;color:var(--white);white-space:nowrap}
.rule{width:82px;height:3px;background:var(--white)}
.body-strong{font-family:"Roboto",sans-serif;font-weight:500;font-size:17px;line-height:34px;color:var(--white)}

/* split */
.split{top:2067px;width:606px;height:397px}
.split.left{left:0;background:linear-gradient(135deg,#1b8fdc,#3aa7ea 60%,#63b8ee)}
.split.right{left:606px;width:594px;background:linear-gradient(135deg,#3b4563,#505b74 60%,#5f6d62)}

/* about */
.about-mark{left:32px;top:2593px;width:530px;height:530px;border-radius:50%;background:radial-gradient(circle at 40% 40%,#8fc6ea,#2f7fbf 55%,#1d4f86)}
.about-copy{left:627px;top:2611px;width:470px}
.about-copy h2{font-family:"DM Sans",sans-serif;font-size:40px;line-height:52px;font-weight:700;color:var(--ink);margin-top:12px;letter-spacing:.5px}
.about-copy p{font-size:15.5px;line-height:24px;margin-top:26px}
.about-copy p + p{margin-top:24px}
.about-copy .btn{margin-top:30px}

/* footer */
.site-footer{left:0;top:3237px;width:1200px;height:588px}
.site-footer .brand .brand-dot{width:56px;height:56px}
.site-footer .brand .brand-name{font-size:30px;color:var(--white)}
.foot-col h3{font-family:"Roboto",sans-serif;font-weight:700;font-size:21px;color:var(--blue);text-transform:uppercase}
.foot-col ul{list-style:none;margin-top:18px}
.foot-col li{font-size:17px;line-height:34px;color:var(--white)}
.contact-row{display:flex;gap:16px;color:var(--white);font-size:17px;line-height:26px}
.contact-row svg{flex:none;margin-top:5px}
.social{display:flex;gap:10px}
.social span{width:46px;height:46px;border-radius:50%;background:var(--navy-deep);border:2px solid #0e1428}
.social span:first-child{background:var(--blue);border-color:var(--blue)}
.foot-rule{left:111px;top:3739px;width:978px;height:1px;background:#3a86c4}
.copyright{left:0;top:3765px;width:1200px;text-align:center;color:var(--white);font-family:"Roboto",sans-serif;font-size:16px}
</style>
</head>
<body>

<header class="site-header abs">
  <a class="brand abs" href="#"><span class="brand-dot"></span><span class="brand-name">Brixel Solutions</span></a>
  <nav class="main-nav abs">
    <a class="active" href="#">Home</a><a href="#">About</a><a href="#">Packaging</a><a href="#">MDF Products</a><a href="#">Industries</a><a href="#">Contact</a>
  </nav>
  <svg class="search-icon abs" width="18" height="18" viewBox="0 0 18 18"><circle cx="7.5" cy="7.5" r="5.5" fill="none" stroke="#24304f" stroke-width="2.5"/><line x1="11.5" y1="11.5" x2="16" y2="16" stroke="#24304f" stroke-width="3" stroke-linecap="round"/></svg>
</header>

<section class="hero abs">
  <svg class="abs" style="left:0;top:0" width="1200" height="694" viewBox="0 0 1200 694">
    <defs>
      <linearGradient id="heroPhoto" x1="0" x2="1" y1="0" y2="0">
        <stop offset="0" stop-color="#1f2a4a"/>
        <stop offset=".45" stop-color="#4d5a72"/>
        <stop offset="1" stop-color="#a89a7e"/>
      </linearGradient>
    </defs>
    <rect width="1200" height="694" fill="#1f2a4a"/>
    <rect x="640" width="560" height="694" fill="url(#heroPhoto)" role="img" aria-label="Warehouse worker in a hard hat carrying a board"/>
    <path d="M0,500 Q600,808 1200,500 L1200,694 L0,694Z" fill="#ffffff"/>
    <path d="M255,612 Q600,724 945,612 Q600,776 255,612Z" fill="#10a0f2"/>
  </svg>
  <div class="hero-copy abs" style="top:89px">
    <h1 class="hero-title"><span class="light">Custom</span><br><span class="accent">Flexible Packaging</span> &amp;<br>MDF Product Solutions</h1>
    <p class="hero-lead">Delivering innovative custom packaging, printed flexible films, laminated structures, and premium MDF products that help manufacturers protect, promote, and grow their brands.</p>
    <a class="btn" href="#">Request a Quote</a>
  </div>
</section>

<section class="intro abs">
  <div class="eyebrow">Packaging</div>
  <h2>Manufacturing Excellence Built Around<br>Your Products</h2>
  <p>Brix-El provides high-quality custom flexible packaging and engineered MDF solutions for manufacturers across multiple industries. From concept to production, we partner with our customers to deliver reliable products, consistent quality, and exceptional service.</p>
</section>

<div class="category abs" style="left:111px"><div class="thumb" role="img" aria-label="Automated packaging line with boxes" style="background:linear-gradient(160deg,#c9d3dd,#7d8a99 60%,#a88a62)"></div><div class="label">Flexible Packaging</div></div>
<div class="category abs" style="left:361px"><div class="thumb" role="img" aria-label="Rolls of blue plastic film" style="background:linear-gradient(160deg,#dde6f0,#6f9cc9 55%,#2d5d8f)"></div><div class="label hl">Rollstock Film</div></div>
<div class="category abs" style="left:609px"><div class="thumb" role="img" aria-label="Hands feeding laminated kraft paper through a machine" style="background:linear-gradient(160deg,#d8cbb8,#b8906a 55%,#8a6a4e)"></div><div class="label">Laminated Packaging</div></div>
<div class="category abs" style="left:858px"><div class="thumb" role="img" aria-label="Stacked MDF panels" style="background:linear-gradient(160deg,#e3d8c8,#c7a887 55%,#6a4a34)"></div><div class="label">MDF Panels</div></div>

<section class="band abs">
  <div class="band-photo abs" role="img" aria-label="Worker in a safety vest handling packaging material"></div>
  <h2 class="section-title abs" style="left:111px;top:66px">Flexible Packaging Solutions</h2>
  <div class="rule abs" style="left:116px;top:135px"></div>
  <p class="body-strong abs" style="left:116px;top:174px;width:920px">Brix-El manufactures custom flexible packaging for food, consumer goods, industrial products, and specialty markets.&nbsp; Brix-El specializes in manufacturing innovative flexible packaging solutions and quality MDF products for customers who value consistency, reliability, and exceptional service.</p>
  <a class="btn abs" href="#" style="left:111px;top:312px">View All Packaging</a>
</section>

<section class="split left abs" role="img" aria-label="Blue tinted rolls of packaging film">
  <h2 class="section-title abs" style="left:111px;top:52px">Custom Flexible Packaging</h2>
  <div class="rule abs" style="left:116px;top:103px"></div>
  <p class="body-strong abs" style="left:116px;top:126px;width:425px">Brix-El manufactures custom flexible packaging for food, consumer goods, industrial products, and specialty markets.</p>
  <a class="btn dark abs" href="#" style="left:111px;top:264px">Learn More</a>
</section>
<section class="split right abs" role="img" aria-label="Worker operating MDF production machinery">
  <h2 class="section-title abs" style="left:79px;top:52px">Engineered MDF Products</h2>
  <div class="rule abs" style="left:84px;top:103px"></div>
  <p class="body-strong abs" style="left:84px;top:126px;width:450px">Brix-El also supplies quality MDF products suitable for furniture manufacturing, cabinetry, interior construction, and industrial applications.</p>
  <a class="btn abs" href="#" style="left:79px;top:264px">Learn More</a>
</section>

<div class="about-mark abs" role="img" aria-label="Large circular panel with blue film rolls"></div>
<section class="about-copy abs">
  <div class="eyebrow">Who We Are</div>
  <h2>Packaging<br>manufacturing line</h2>
  <p>Brix-El provides high-quality custom flexible packaging and engineered MDF solutions for manufacturers across multiple industries. From concept to production, we partner with our customers to deliver reliable products, consistent quality, and exceptional service.</p>
  <p>Whether you need printed pouches, rollstock films, laminated packaging, or MDF panels, our experienced team ensures every project meets the highest manufacturing standards.</p>
  <a class="btn" href="#">Read More</a>
</section>

<footer class="site-footer abs">
  <svg class="abs" style="left:0;top:0" width="1200" height="588" viewBox="0 0 1200 588">
    <path d="M0,193 Q600,-29 1200,193 L1200,588 L0,588Z" fill="#1f2a4a"/>
    <path d="M270,67 Q600,-67 935,67 Q600,-3 270,67Z" fill="#10a0f2"/>
  </svg>
  <a class="brand abs" href="#" style="left:119px;top:238px"><span class="brand-dot"></span><span class="brand-name">Brixel Solutions</span></a>
  <div class="social abs" style="left:113px;top:347px"><span></span><span></span><span></span><span></span></div>
  <div class="foot-col abs" style="left:549px;top:225px">
    <h3>Quick Links</h3>
    <ul style="margin-left:4px"><li>Home</li><li>About</li><li>Packaging</li><li>Mdf Products</li><li>Industries</li><li>Contact</li></ul>
  </div>
  <div class="foot-col abs" style="left:783px;top:225px;width:310px">
    <h3>Get In Touch</h3>
    <div class="contact-row" style="margin-top:20px"><svg width="17" height="20" viewBox="0 0 17 20"><path d="M8.5 0C4 0 1 3.2 1 7.3 1 12.5 8.5 20 8.5 20S16 12.5 16 7.3C16 3.2 13 0 8.5 0Z" fill="#10a0f2"/><circle cx="8.5" cy="7.3" r="2.8" fill="#1f2a4a"/></svg><span>1245&nbsp; ipsum dolor sit amet, consectetur adipiscing elit,</span></div>
    <div class="contact-row" style="margin-top:30px"><svg width="17" height="17" viewBox="0 0 24 24"><path d="M6.6 10.8a15 15 0 006.6 6.6l2.2-2.2c.3-.3.7-.4 1-.2 1.1.4 2.3.6 3.6.6.6 0 1 .4 1 1V20c0 .6-.4 1-1 1C10.6 21 3 13.4 3 4c0-.6.4-1 1-1h3.5c.6 0 1 .4 1 1 0 1.300.2 2.500.6 3.600.1.300 0 .700-.2 1z" fill="#10a0f2"/></svg><span>+1 888-888-8888</span></div>
    <div class="contact-row" style="margin-top:34px"><svg width="20" height="16" viewBox="0 0 20 16"><rect width="20" height="16" rx="2" fill="#10a0f2"/><path d="M1 2l9 7 9-7" fill="none" stroke="#1f2a4a" stroke-width="1.8"/></svg><span>info@brixelsolutions.com</span></div>
  </div>
</footer>
<div class="foot-rule abs"></div>
<p class="copyright abs">Copyright 2026 Company Name All Rights Reserved</p>

</body>
</html>
```